New Website - vantomix.com

This is what we looking for - http://www.sketchpoolery.com/design/738412
Updates

hello, im back and i want some good designs for my website.. i need really creative ideas. this is for a cellphone provider company. Vantomix mobile please provide me a good ideas and i will go with u also to program the website

Font styles to use
Sans Serif

```html
<!DOCTYPE html>
<html lang="en">
<head>
<meta charset="utf-8">
<title>Vantomix Communications</title>
<link href="https://fonts.googleapis.com/css2?family=Cantarell:wght@400;700&family=Raleway:wght@300;400;600&family=Arimo:wght@400;700&display=swap" rel="stylesheet">
<style>
:root{
  --bg:#f3f3f3;
  --ink:#333;
  --muted:#555;
  --blue:#1a86c8;
  --blue-light:#4fb8ee;
  --dark:#222;
  --hero:#1e1e1e;
  --panel:#fff;
  --line:#dcdcdc;
  --footer:#d9d9d9;
  --strip:#17a4e8;
}
*{box-sizing:border-box;margin:0;padding:0}
html,body{width:1038px;height:1200px;overflow:hidden;background:var(--bg);font-family:Arimo,Arial,sans-serif;color:var(--ink)}
.page{position:relative;width:1038px;height:1200px;overflow:hidden;background:linear-gradient(180deg,#fafafa 0,#f1f1f1 100%)}
.abs{position:absolute}

/* top nav */
.topnav{left:86px;top:22px;width:865px;height:55px;background:#ececec;display:flex}
.topnav a{display:block;padding:14px 0 0 16px;text-decoration:none;font-family:Cantarell,sans-serif;color:#8a8a8a;font-size:16px;line-height:1;border-right:1px solid #d6d6d6}
.topnav a small{display:block;font-family:Arimo,sans-serif;font-size:9px;margin-top:5px}
.topnav a.active{background:#2e2e2e;color:#fff;width:78px}
.topnav .office{width:105px}.topnav .cell{width:110px;border:none}
.search{left:746px;top:35px;width:191px;height:32px;border-radius:16px;background:linear-gradient(#e2e2e2,#f7f7f7);border:1px solid #ccc;font-size:10px;color:#999;padding:10px 0 0 17px}
.search svg{position:absolute;right:14px;top:8px}

/* brand */
.brand{left:95px;top:122px;display:flex;align-items:center;gap:10px}
.brand-mark{width:46px;height:46px;border-radius:50%;background:var(--blue-light)}
.brand-name{font-family:Cantarell,sans-serif;font-size:40px;color:var(--blue-light);line-height:1}
.brand-sub{left:171px;top:162px;font-family:Cantarell,sans-serif;font-size:14px;letter-spacing:2.5px;color:var(--ink)}

.subnav{left:666px;top:161px;display:flex;gap:2px}
.subnav a{display:block;height:34px;width:91px;background:linear-gradient(#ededed,#d9d9d9);font-size:12px;color:#444;text-align:center;padding-top:12px;text-decoration:none}
.subnav a.account{width:100px;text-align:left;padding-left:14px}
.subnav a.account span{display:inline-block;width:14px;height:13px;background:#fff;border:1px solid #bbb;margin-left:5px;vertical-align:middle;position:relative}
.subnav a.account span:after{content:"";position:absolute;left:3px;top:4px;border:3px solid transparent;border-top:4px solid #555}

/* hero */
.hero{left:86px;top:197px;width:865px;height:317px;border-radius:4px;background:repeating-linear-gradient(90deg,#1c1c1c 0 2px,#232323 2px 4px);box-shadow:0 10px 14px -8px rgba(0,0,0,.4)}
.hero h1{position:absolute;left:46px;top:95px;font-family:Raleway,sans-serif;font-weight:400;font-size:32px;color:#2a95dc;white-space:nowrap}
.hero p.l1{position:absolute;left:46px;top:138px;font-family:Raleway,sans-serif;font-weight:300;font-size:22px;color:#ddd}
.hero p.l2{position:absolute;left:46px;top:170px;font-family:Raleway,sans-serif;font-weight:300;font-size:22px;color:#2a95dc}
.hero .cta{position:absolute;left:46px;top:223px;width:205px;height:43px;border-radius:10px;background:linear-gradient(#fbfbfb,#c8c8c8);font-family:Cantarell,sans-serif;font-weight:700;font-size:23px;color:#444;text-align:center;padding-top:7px;letter-spacing:.5px}
.hero .phone{position:absolute;left:619px;top:84px;width:208px;height:212px;border-radius:14px;background:linear-gradient(135deg,#3a3a3a,#0e0e0e)}

/* about */
.about{left:85px;top:532px;width:861px;height:236px;background:linear-gradient(#fff,#f4f4f4);border:1px solid #ddd;border-radius:3px}
.video{left:14px;top:16px;width:296px;height:198px;background:linear-gradient(120deg,#cfd9e4,#eef2f5 55%,#d8dde2);border:2px solid #ccc}
.video .bar{position:absolute;left:0;bottom:0;width:100%;height:14px;background:#222}
.video .bar i{position:absolute;left:58px;top:4px;width:60px;height:6px;background:#3a6fd0}
.video .play{position:absolute;left:118px;top:55px}
.about h2{position:absolute;left:329px;top:17px;font-family:Cantarell,sans-serif;font-weight:400;font-size:19px;color:var(--blue)}
.about .copy{position:absolute;left:331px;top:41px;width:513px;font-size:12px;line-height:19px;color:var(--muted);text-align:justify}
.about .copy b{color:#333}
.about .copy p+p{margin-top:19px}
.about .more{position:absolute;left:331px;top:187px;width:84px;height:27px;background:#333;color:#fff;font-size:12px;text-align:center;padding-top:7px}

/* features */
.features{left:86px;top:785px;width:865px;height:245px;background:#fff;border-radius:4px}
.divider{top:45px;width:1px;height:200px;background:var(--line)}
.col{top:52px}
.col h3{font-family:Cantarell,sans-serif;font-weight:400;font-size:19px;color:var(--blue)}
.col .lead{font-size:12.5px;font-weight:700;color:#444;margin-top:8px;letter-spacing:.2px}
.col ul{list-style:none;margin-top:13px}
.col li{font-size:11px;color:#444;height:24px;padding-left:13px;position:relative}
.col li:before{content:"";position:absolute;left:0;top:4px;width:6px;height:6px;border-radius:50%;background:var(--blue)}
.col .link{font-size:12px;font-style:italic;color:var(--blue);text-decoration:underline;display:inline-block;margin-top:1px}
.col .link:after{content:"›";font-style:normal;display:inline-block;margin-left:6px;text-decoration:none;font-weight:700}
.keep{font-size:14.5px;font-weight:700;color:#333;margin-top:12px;letter-spacing:.4px}
.inputs{display:flex;gap:11px;margin-top:14px}
.inputs span{display:block;width:65px;height:26px;border:1px solid #ccc;background:#fff}
.inputs span:nth-child(2){margin-left:0}
.check{display:block;margin-top:15px;margin-left:3px;width:198px;height:36px;background:linear-gradient(#2c9ae6,#0d6ab4);border:1px solid #0b5f9f;color:#fff;font-family:Cantarell,sans-serif;font-weight:700;font-size:18px;text-align:center;padding-top:7px}

/* footer */
.footer{left:0;top:1081px;width:1038px;height:113px;background:var(--footer);border-top:1px dotted #999}
.strip{left:0;top:1194px;width:1038px;height:6px;background:var(--strip)}
.fnav{left:88px;top:1112px;display:flex;font-size:11px;font-weight:700;color:#555}
.fnav span{margin-right:29px}
.copyright{left:89px;top:1145px;font-size:11px;color:#444}
.follow{left:782px;top:1110px;font-family:Cantarell,sans-serif;font-weight:700;font-size:16px;color:#666}
.social{top:1106px;width:26px;height:26px;border-radius:50%}
.legal{left:705px;top:1145px;font-size:11px;color:#444;word-spacing:2px}
</style>
</head>
<body>
<div class="page">

  <nav class="topnav abs">
    <a class="active" href="#">Home<small>In Your</small></a>
    <a class="office" href="#">Office<small>In Your</small></a>
    <a class="cell" href="#">Cellphone<small>In Your</small></a>
  </nav>
  <div class="search abs">Search here...
    <svg width="18" height="16" viewBox="0 0 18 16"><circle cx="7" cy="6.5" r="5" fill="none" stroke="#3aa3e3" stroke-width="2"/><line x1="10.5" y1="10" x2="16" y2="14.5" stroke="#3aa3e3" stroke-width="2.5" stroke-linecap="round"/></svg>
  </div>

  <div class="brand abs"><span class="brand-mark"></span><span class="brand-name">Vantomix</span></div>
  <div class="brand-sub abs">COMMUNICATIONS</div>

  <nav class="subnav abs">
    <a href="#">Support</a><a href="#">Contact</a><a class="account" href="#">My Account<span></span></a>
  </nav>

  <section class="hero abs">
    <h1>A Revolutionary Digital Phone Service</h1>
    <p class="l1">that will Save you, your family, &amp; Your</p>
    <p class="l2">Business lots of Money</p>
    <div class="cta">Sign Up Today</div>
    <div class="phone" role="img" aria-label="Black office desk phone with display and keypad"></div>
  </section>

  <section class="about abs">
    <div class="video abs" role="img" aria-label="Video still of call centre agents wearing headsets">
      <svg class="play" width="60" height="60" viewBox="0 0 60 60"><circle cx="30" cy="30" r="28" fill="#222" stroke="#ddd" stroke-width="3"/><path d="M23 17 L44 30 L23 43 Z" fill="#fff"/></svg>
      <div class="bar"><i></i></div>
    </div>
    <h2>About Us</h2>
    <div class="copy">
      <p><b>Lorem ipsum dolor sit amet, consectetur adipisicing elit, sed do eiusmod tempor incididunt ut labore et dolore magna aliqua</b>. Ut enim ad minim veniam, quis nostrud exercitation ullamco laboris commodo consequat.</p>
      <p>Duis aute irure dolor in reprehenderit in voluptate velit esse cillum dolore eu fugiat nulla pariatur. Excepteur sint occaecat cupidatat non proident, sunt in culpa qui officia deserunt mollit anim id est laborum. pariatur. Stet clita kasd gubergren, no sea takimata est.</p>
    </div>
    <div class="more">Read More</div>
  </section>

  <section class="features abs">
    <div class="divider abs" style="left:276px"></div>
    <div class="divider abs" style="left:587px"></div>
    <div class="col abs" style="left:37px">
      <h3>Affordable</h3>
      <p class="lead">Starting Saving Today!</p>
      <ul><li>simply dummy text of the printing</li><li>Lorem Ipsum has been the industry's</li><li>Lorem Ipsum has been the industry's</li><li>Lorem Ipsum has been the industry's</li></ul>
      <a class="link" href="#">Compare rates &amp; Plans</a>
    </div>
    <div class="col abs" style="left:327px;top:51px">
      <h3>Powerful</h3>
      <p class="lead">Starting Saving Today!</p>
      <ul><li>simply dummy text of the printing</li><li>Lorem Ipsum has been the industry's</li><li>Lorem Ipsum has been the industry's</li><li>Lorem Ipsum has been the industry's</li></ul>
      <a class="link" href="#">Compare rates &amp; Plans</a>
    </div>
    <div class="col abs" style="left:630px;top:56px">
      <h3>Flexible</h3>
      <p class="lead">Service On Your Own Terms</p>
      <p class="keep">KEEP YOUR NAME</p>
      <div class="inputs"><span></span><span></span><span></span></div>
      <span class="check">Check Availability</span>
    </div>
  </section>

  <footer class="footer abs"></footer>
  <div class="fnav abs"><span>Home</span><span>|</span><span>Services</span><span>|</span><span>Clients</span><span>|</span><span>Contact Us</span><span>|</span><span>Blog</span></div>
  <div class="copyright abs">Copyright © Corvello Digital 2011–2012. All rights reserved.</div>
  <div class="follow abs">Follow us</div>
  <span class="social abs" style="left:862px;background:#7cc3ea"></span>
  <span class="social abs" style="left:898px;background:#3b5c9c"></span>
  <div class="legal abs">Press &nbsp;|&nbsp; Privacy Policy &nbsp;|&nbsp; User Agreement</div>
  <div class="strip abs"></div>

</div>
</body>
</html>
```